Local electrical company needs two flyers designed

We are a small local electrical contracting company and are in desperate need of a awasome flyer design to help grow our business

hi everyone.

please keep the logo off the front page.
it can go on the rear.

We are really trying to portray a angry/frustrated women BECAUSE her lights are broken.
not light globes

Target Market(s)

Home owners

Industry/Entity Type

Electrical

Font styles to use
Serif

Requirements
Nice to have

```html
<!DOCTYPE html>
<html lang="en">
<head>
<meta charset="utf-8">
<title>Brightline Power – LED Downlights Flyer</title>
<link rel="stylesheet" href="https://fonts.googleapis.com/css2?family=Gelasio:wght@400;700&family=Open+Sans:wght@400&display=swap">
<style>
  :root {
    --paper: #ffffff;
    --frame: #444444;
    --yellow: #fbec00;
    --yellow-deep: #e4d21e;
    --green: #006233;
    --ink: #1e1e1e;
    --tick: #d6331f;
    --white: #ffffff;
    --card-line: #222222;
  }
  * { margin: 0; padding: 0; box-sizing: border-box; }
  html, body { width: 1200px; height: 840px; overflow: hidden; background: var(--paper); }
  .canvas {
    position: relative; width: 1200px; height: 840px;
    background: var(--paper); border: 1px solid var(--frame);
    font-family: "Gelasio", Georgia, serif; color: var(--ink);
  }
  .flyer {
    position: absolute; left: 58px; top: 58px; width: 1085px; height: 725px;
    background: var(--yellow); border: 1px solid var(--ink); overflow: hidden;
  }
  .skyline {
    position: absolute; left: 0; top: 300px; width: 100%; height: 280px;
    background: linear-gradient(180deg, rgba(228,210,30,0) 0%, rgba(228,210,30,0.7) 45%, var(--yellow-deep) 100%);
  }
  .call-box {
    position: absolute; right: 0; top: 0; width: 434px; height: 84px;
    background: var(--green); color: var(--white);
    font-size: 38px; line-height: 84px; padding-left: 26px;
  }
  .intro {
    position: absolute; left: 61px; top: 100px; width: 900px;
    font-size: 20.5px; line-height: 34px; white-space: nowrap;
  }
  .offer { position: absolute; left: 61px; top: 168px; font-size: 21px; white-space: nowrap; }
  .offer .amount { font-size: 40px; font-weight: 700; }
  .offer strong { font-weight: 700; }
  .offer sup { font-size: 12px; }
  .benefits { position: absolute; left: 46px; top: 245px; list-style: none; font-size: 24px; line-height: 42.5px; }
  .benefits li { display: flex; align-items: center; gap: 4px; }
  .benefits svg { width: 16px; height: 16px; }
  .payment-card {
    position: absolute; border: 2px solid var(--card-line); background: var(--white);
    display: flex; align-items: center; justify-content: center;
    font-size: 17px; color: var(--ink);
  }
  .card-a { left: 70px; top: 428px; width: 110px; height: 70px; }
  .card-b { left: 184px; top: 428px; width: 108px; height: 72px; }
  .card-c { left: 137px; top: 504px; width: 98px; height: 72px; border-color: #c9c9c9; }
  .mascot {
    position: absolute; left: 910px; top: 168px; width: 160px; height: 130px;
    background: radial-gradient(circle at 50% 45%, #8fc63f 0%, #2f8a3a 60%, rgba(47,138,58,0) 100%);
  }
  .brand-name {
    position: absolute; left: 805px; top: 308px; width: 260px;
    font-size: 26px; font-weight: 700; color: var(--green); line-height: 30px;
  }
  .testimonial {
    position: absolute; right: 25px; top: 397px; width: 600px; text-align: right;
    font-family: "Open Sans", Arial, sans-serif; font-size: 17px; line-height: 22.5px;
  }
  .footer-band {
    position: absolute; left: 0; bottom: 0; width: 100%; height: 146px;
    background: var(--green); color: var(--white); text-align: center;
    font-size: 24px; line-height: 34px; padding-top: 14px;
  }
</style>
</head>
<body>
<div class="canvas">
  <div class="flyer">
    <div class="skyline" role="img" aria-label="Faint city skyline silhouette in muted yellow tones"></div>

    <div class="call-box">Call now 1300 555 018</div>

    <p class="intro">For more information visit www.brightlinepower.com.au/leddownlights<br>
      Replace your old $$$ burning halogen downlights with new money saving led downlights</p>

    <p class="offer">Offer: <span class="amount">Save $25 off</span> every 3<sup>rd</sup> <strong>downlight replaced (stand out offer)</strong></p>

    <ul class="benefits">
      <li><svg viewBox="0 0 16 16"><path d="M2 9 L6 13 L14 3" fill="none" stroke="var(--tick)" stroke-width="1.6"/></svg>Specialising in domestic electrical repairs</li>
      <li><svg viewBox="0 0 16 16"><path d="M2 9 L6 13 L14 3" fill="none" stroke="var(--tick)" stroke-width="1.6"/></svg>On Time guarantee or $100 OFF</li>
      <li><svg viewBox="0 0 16 16"><path d="M2 9 L6 13 L14 3" fill="none" stroke="var(--tick)" stroke-width="1.6"/></svg>Up front pricing</li>
      <li><svg viewBox="0 0 16 16"><path d="M2 9 L6 13 L14 3" fill="none" stroke="var(--tick)" stroke-width="1.6"/></svg>No mess guaranteed</li>
    </ul>

    <div class="payment-card card-a">Paywise</div>
    <div class="payment-card card-b">Cardmark</div>
    <div class="payment-card card-c">Globepay</div>

    <div class="mascot" role="img" aria-label="Cartoon superhero electrician holding up a light bulb"></div>
    <div class="brand-name">Brightline Power Pty Ltd</div>

    <blockquote class="testimonial">“Excellent electrician! Turns up on time,<br>
      friendly and a can-do attitude.<br>
      Did several jobs here including installing (and recommending)<br>
      LED lights in our kitchen and dining room. No mess, quick and<br>
      efficient. Highly recommended”<br>
      R.Castell Ashbury</blockquote>

    <div class="footer-band">
      <p>www.brightlinepower.com.au</p>
      <p>*Mention this ad when booking to receive offer. Limit one per household</p>
      <p>*Cannot be combined with any other offer</p>
    </div>
  </div>
</div>
</body>
</html>
```